Trendy E Juice Product Labels Required

We are looking for design for an e Juice label line (the liquids used in electronic cigarettes). What we need is 5 product labels which eventually will be printed on 95mm x 40mm labels. Obviously the image will be created much larger than this but the aspect ratio should be scalable down to this size.

What each label must have is I would need is a background, a monster character, and space for a product name incorporated in to the design. The brand on this line is "Brisk Lantern". Whilst creatively, we are completely open to any concept, there is certain text which is necessary for incorporation in to each label. The attached file, "Example Label" shows these elements. NOTE: the attached file IS NOT a finished label.
Updates

Project Deadline Extended
Reason: Not received a design that we wish to proceed with.

Target Market(s)

25-35 year old vapers

Industry/Entity Type

Electronic

Requirements
Should not have
• Anything that may be construed as being targeted toward children.

```html
<!DOCTYPE html>
<html lang="en">
<head>
<meta charset="utf-8">
<title>Brisk Lantern – E-Liquid Label Range</title>
<link href="https://fonts.googleapis.com/css2?family=Oswald:wght@500&family=Open+Sans:wght@400;700&family=Alegreya+SC:wght@700&display=swap" rel="stylesheet">
<style>
  :root{
    --teal:#235a63;
    --ink:#111;
    --paper:#ffffff;
    --stage:#eceded;
    --hazard:#e0262b;
    --banana:#d3d749;
    --melon:#f7bddb;
    --orange:#f5da8b;
    --straw:#fbf6aa;
    --apple:#88d5d7;
  }
  *{box-sizing:border-box;margin:0;padding:0}
  html,body{width:1200px;height:1000px;overflow:hidden}
  body{background:radial-gradient(ellipse at 50% 45%,#fafafa 0%,var(--stage) 80%);font-family:"Open Sans",sans-serif;color:var(--ink);position:relative}

  .label{position:absolute;width:470px;height:200px;background:var(--paper);overflow:hidden;box-shadow:0 3px 6px rgba(0,0,0,.25)}
  .label.banana{left:370px;top:95px;--accent:var(--banana);--creature:#8a4a2a}
  .label.melon{left:118px;top:360px;--accent:var(--melon);--creature:#3f5dab}
  .label.orange{left:622px;top:360px;--accent:var(--orange);--creature:#c8373a}
  .label.straw{left:118px;top:622px;--accent:var(--straw);--creature:#c0379b}
  .label.apple{left:622px;top:622px;--accent:var(--apple);--creature:#4b7a3a}

  .band-top,.band-bottom{position:absolute;left:0;width:100%;height:12px;background:var(--teal)}
  .band-top{top:0}
  .band-bottom{bottom:0;height:13px}
  .colour-band{position:absolute;left:0;top:124px;width:100%;height:63px;background:var(--accent);border-top:3px solid var(--ink)}

  .warning,.ingredients{position:absolute;left:8px;width:170px;text-align:center;font-size:6.3px;line-height:9px;text-transform:uppercase;white-space:nowrap;z-index:2}
  .warning{top:18px}
  .ingredients{top:133px}
  .warning h3,.ingredients h3{font-size:6.6px;font-weight:700}

  .character{position:absolute;left:186px;top:12px;width:130px;height:112px;z-index:1;
    background:radial-gradient(circle at 50% 90%,var(--creature) 0 30%,#f7e3b0 31%,#fff6dc 70%,#fff 100%)}

  .brand-plate{position:absolute;left:155px;top:104px;width:152px;height:44px;background:var(--paper);border:3px solid var(--ink);z-index:3;
    display:flex;align-items:center;justify-content:center;transform:rotate(-1.5deg)}
  .brand-name{font-family:"Oswald",sans-serif;font-weight:500;font-size:22px;letter-spacing:.3px;white-space:nowrap}
  .flavour{position:absolute;left:165px;top:158px;width:140px;text-align:center;font-family:"Alegreya SC",serif;font-weight:700;font-size:13px;letter-spacing:.5px;border-bottom:1px solid var(--ink);padding-bottom:1px;z-index:2}

  .web{position:absolute;left:330px;top:18px;width:120px;text-align:center;font-size:6.8px;font-weight:700}
  .social{position:absolute;left:346px;top:30px;display:flex;gap:4px}
  .social span{width:24px;height:24px;border:1.5px solid var(--ink);border-radius:50%}
  .handle{position:absolute;left:330px;top:60px;width:120px;text-align:center;font-size:6.8px;font-weight:700}
  .distributor{position:absolute;left:322px;top:75px;width:134px;height:40px;background:var(--accent);border:2px solid var(--ink);border-radius:5px;
    display:flex;flex-direction:column;align-items:center;justify-content:center;text-align:center;font-size:6.6px;font-weight:700;line-height:9px;text-transform:uppercase;white-space:nowrap}

  .pictograms{position:absolute;left:342px;top:138px}
  .hazard-triangle{position:absolute;left:396px;top:138px}
</style>
</head>
<body>

<section class="label banana">
  <div class="band-top"></div>
  <div class="warning"><h3>Warning</h3>This product contains nicotine,<br>a substance which is known to cause<br>birth defects. Do not swallow. Avoid<br>contact with skin. Keep out of reach<br>of children and pets. This product is<br>intended for use by persons 18 and<br>older. Pregnant women and those<br>breast feeding should not use this<br>product. May contain traces of nuts.</div>
  <div class="colour-band"></div>
  <div class="ingredients"><h3>Ingredients</h3>USP/EP propylene glycol (xx%),<br>USP/EP vegetable glycerin<br>(xx%), USP/EP nicotine, natural<br>and artificial flavorings.</div>
  <div class="character" role="img" aria-label="Brown cartoon creature with eye stalks on a sunburst"></div>
  <div class="brand-plate"><span class="brand-name">BRISK LANTERN</span></div>
  <div class="flavour">BANANA</div>
  <div class="web">WWW.DOMAINNAME.COM</div>
  <div class="social" aria-label="Social media"><span></span><span></span><span></span></div>
  <div class="handle">@USERNAME</div>
  <div class="distributor">Distributed by<br>Company Name &amp; Address<br>Telephone</div>
  <svg class="pictograms" width="48" height="44" viewBox="0 0 48 44" aria-hidden="true">
    <g fill="none" stroke="#e0262b" stroke-width="1.6"><circle cx="7" cy="10" r="5.5"/><circle cx="41" cy="10" r="5.5"/><circle cx="7" cy="31" r="5.5"/><circle cx="41" cy="31" r="5.5"/></g>
    <path d="M24 3 L33 18 L15 18 Z" fill="#fff" stroke="#111" stroke-width="1.4"/><rect x="23.3" y="8" width="1.4" height="5" fill="#111"/><rect x="23.3" y="14.3" width="1.4" height="1.4" fill="#111"/>
    <text x="41" y="33.5" font-size="7" font-weight="700" text-anchor="middle" font-family="Open Sans,sans-serif">18</text>
  </svg>
  <svg class="hazard-triangle" width="54" height="46" viewBox="0 0 54 46" aria-hidden="true"><path d="M27 3 L51 43 L3 43 Z" fill="none" stroke="#e0262b" stroke-width="2.6"/></svg>
  <div class="band-bottom"></div>
</section>

<section class="label melon">
  <div class="band-top"></div>
  <div class="warning"><h3>Warning</h3>This product contains nicotine,<br>a substance which is known to cause<br>birth defects. Do not swallow. Avoid<br>contact with skin. Keep out of reach<br>of children and pets. This product is<br>intended for use by persons 18 and<br>older. Pregnant women and those<br>breast feeding should not use this<br>product. May contain traces of nuts.</div>
  <div class="colour-band"></div>
  <div class="ingredients"><h3>Ingredients</h3>USP/EP propylene glycol (xx%),<br>USP/EP vegetable glycerin<br>(xx%), USP/EP nicotine, natural<br>and artificial flavorings.</div>
  <div class="character" role="img" aria-label="Spiky blue cartoon creature on a sunburst"></div>
  <div class="brand-plate"><span class="brand-name">BRISK LANTERN</span></div>
  <div class="flavour">MELON</div>
  <div class="web">WWW.DOMAINNAME.COM</div>
  <div class="social" aria-label="Social media"><span></span><span></span><span></span></div>
  <div class="handle">@USERNAME</div>
  <div class="distributor">Distributed by<br>Company Name &amp; Address<br>Telephone</div>
  <svg class="pictograms" width="48" height="44" viewBox="0 0 48 44" aria-hidden="true">
    <g fill="none" stroke="#e0262b" stroke-width="1.6"><circle cx="7" cy="10" r="5.5"/><circle cx="41" cy="10" r="5.5"/><circle cx="7" cy="31" r="5.5"/><circle cx="41" cy="31" r="5.5"/></g>
    <path d="M24 3 L33 18 L15 18 Z" fill="#fff" stroke="#111" stroke-width="1.4"/><rect x="23.3" y="8" width="1.4" height="5" fill="#111"/><rect x="23.3" y="14.3" width="1.4" height="1.4" fill="#111"/>
    <text x="41" y="33.5" font-size="7" font-weight="700" text-anchor="middle" font-family="Open Sans,sans-serif">18</text>
  </svg>
  <svg class="hazard-triangle" width="54" height="46" viewBox="0 0 54 46" aria-hidden="true"><path d="M27 3 L51 43 L3 43 Z" fill="none" stroke="#e0262b" stroke-width="2.6"/></svg>
  <div class="band-bottom"></div>
</section>

<section class="label orange">
  <div class="band-top"></div>
  <div class="warning"><h3>Warning</h3>This product contains nicotine,<br>a substance which is known to cause<br>birth defects. Do not swallow. Avoid<br>contact with skin. Keep out of reach<br>of children and pets. This product is<br>intended for use by persons 18 and<br>older. Pregnant women and those<br>breast feeding should not use this<br>product. May contain traces of nuts.</div>
  <div class="colour-band"></div>
  <div class="ingredients"><h3>Ingredients</h3>USP/EP propylene glycol (xx%),<br>USP/EP vegetable glycerin<br>(xx%), USP/EP nicotine, natural<br>and artificial flavorings.</div>
  <div class="character" role="img" aria-label="Red horned cartoon creature on a sunburst"></div>
  <div class="brand-plate"><span class="brand-name">BRISK LANTERN</span></div>
  <div class="flavour">ORANGES</div>
  <div class="web">WWW.DOMAINNAME.COM</div>
  <div class="social" aria-label="Social media"><span></span><span></span><span></span></div>
  <div class="handle">@USERNAME</div>
  <div class="distributor">Distributed by<br>Company Name &amp; Address<br>Telephone</div>
  <svg class="pictograms" width="48" height="44" viewBox="0 0 48 44" aria-hidden="true">
    <g fill="none" stroke="#e0262b" stroke-width="1.6"><circle cx="7" cy="10" r="5.5"/><circle cx="41" cy="10" r="5.5"/><circle cx="7" cy="31" r="5.5"/><circle cx="41" cy="31" r="5.5"/></g>
    <path d="M24 3 L33 18 L15 18 Z" fill="#fff" stroke="#111" stroke-width="1.4"/><rect x="23.3" y="8" width="1.4" height="5" fill="#111"/><rect x="23.3" y="14.3" width="1.4" height="1.4" fill="#111"/>
    <text x="41" y="33.5" font-size="7" font-weight="700" text-anchor="middle" font-family="Open Sans,sans-serif">18</text>
  </svg>
  <svg class="hazard-triangle" width="54" height="46" viewBox="0 0 54 46" aria-hidden="true"><path d="M27 3 L51 43 L3 43 Z" fill="none" stroke="#e0262b" stroke-width="2.6"/></svg>
  <div class="band-bottom"></div>
</section>

<section class="label straw">
  <div class="band-top"></div>
  <div class="warning"><h3>Warning</h3>This product contains nicotine,<br>a substance which is known to cause<br>birth defects. Do not swallow. Avoid<br>contact with skin. Keep out of reach<br>of children and pets. This product is<br>intended for use by persons 18 and<br>older. Pregnant women and those<br>breast feeding should not use this<br>product. May contain traces of nuts.</div>
  <div class="colour-band"></div>
  <div class="ingredients"><h3>Ingredients</h3>USP/EP propylene glycol (xx%),<br>USP/EP vegetable glycerin<br>(xx%), USP/EP nicotine, natural<br>and artificial flavorings.</div>
  <div class="character" role="img" aria-label="Magenta one-eyed cartoon creature on a sunburst"></div>
  <div class="brand-plate"><span class="brand-name">BRISK LANTERN</span></div>
  <div class="flavour">STRAWBERRY</div>
  <div class="web">WWW.DOMAINNAME.COM</div>
  <div class="social" aria-label="Social media"><span></span><span></span><span></span></div>
  <div class="handle">@USERNAME</div>
  <div class="distributor">Distributed by<br>Company Name &amp; Address<br>Telephone</div>
  <svg class="pictograms" width="48" height="44" viewBox="0 0 48 44" aria-hidden="true">
    <g fill="none" stroke="#e0262b" stroke-width="1.6"><circle cx="7" cy="10" r="5.5"/><circle cx="41" cy="10" r="5.5"/><circle cx="7" cy="31" r="5.5"/><circle cx="41" cy="31" r="5.5"/></g>
    <path d="M24 3 L33 18 L15 18 Z" fill="#fff" stroke="#111" stroke-width="1.4"/><rect x="23.3" y="8" width="1.4" height="5" fill="#111"/><rect x="23.3" y="14.3" width="1.4" height="1.4" fill="#111"/>
    <text x="41" y="33.5" font-size="7" font-weight="700" text-anchor="middle" font-family="Open Sans,sans-serif">18</text>
  </svg>
  <svg class="hazard-triangle" width="54" height="46" viewBox="0 0 54 46" aria-hidden="true"><path d="M27 3 L51 43 L3 43 Z" fill="none" stroke="#e0262b" stroke-width="2.6"/></svg>
  <div class="band-bottom"></div>
</section>

<section class="label apple">
  <div class="band-top"></div>
  <div class="warning"><h3>Warning</h3>This product contains nicotine,<br>a substance which is known to cause<br>birth defects. Do not swallow. Avoid<br>contact with skin. Keep out of reach<br>of children and pets. This product is<br>intended for use by persons 18 and<br>older. Pregnant women and those<br>breast feeding should not use this<br>product. May contain traces of nuts.</div>
  <div class="colour-band"></div>
  <div class="ingredients"><h3>Ingredients</h3>USP/EP propylene glycol (xx%),<br>USP/EP vegetable glycerin<br>(xx%), USP/EP nicotine, natural<br>and artificial flavorings.</div>
  <div class="character" role="img" aria-label="Green cartoon creature with antlers on a sunburst"></div>
  <div class="brand-plate"><span class="brand-name">BRISK LANTERN</span></div>
  <div class="flavour">APPLE</div>
  <div class="web">WWW.DOMAINNAME.COM</div>
  <div class="social" aria-label="Social media"><span></span><span></span><span></span></div>
  <div class="handle">@USERNAME</div>
  <div class="distributor">Distributed by<br>Company Name &amp; Address<br>Telephone</div>
  <svg class="pictograms" width="48" height="44" viewBox="0 0 48 44" aria-hidden="true">
    <g fill="none" stroke="#e0262b" stroke-width="1.6"><circle cx="7" cy="10" r="5.5"/><circle cx="41" cy="10" r="5.5"/><circle cx="7" cy="31" r="5.5"/><circle cx="41" cy="31" r="5.5"/></g>
    <path d="M24 3 L33 18 L15 18 Z" fill="#fff" stroke="#111" stroke-width="1.4"/><rect x="23.3" y="8" width="1.4" height="5" fill="#111"/><rect x="23.3" y="14.3" width="1.4" height="1.4" fill="#111"/>
    <text x="41" y="33.5" font-size="7" font-weight="700" text-anchor="middle" font-family="Open Sans,sans-serif">18</text>
  </svg>
  <svg class="hazard-triangle" width="54" height="46" viewBox="0 0 54 46" aria-hidden="true"><path d="M27 3 L51 43 L3 43 Z" fill="none" stroke="#e0262b" stroke-width="2.6"/></svg>
  <div class="band-bottom"></div>
</section>

</body>
</html>
```